Coverseite für Einladungskarte DIN Lang
Zielgruppe
Die Heilkundliche Gemeinschaft Südwestfalen (www.gbwl-heilkunde.de)
Die ambulante Versorgung
Alle Ärzte, Psychologische Psychotherapeuten sowie Kinder- und Jugendlichenpsychotherapeuten in Nordrhein, die Kassenpatienten behandeln, sind in der Heilkundlichen Gemeinschaft (HG) Südwestfalen zusammengeschlossen, um die ambulante medizinische Versorgung der Bevölkerung sicherzustellen. Zugleich ist die HG Südwestfalen Interessenvertreter ihrer Mitglieder.
Die rund 18 500 Vertragsärzte, Psychologischen Psychotherapeuten, Kinder- und Jugendlichenpsychotherapeuten sowie zur ambulanten Behandlung ermächtigten Krankenhausärzte stellen die Versorgung von 9,5 Millionen Menschen in Nordrhein sicher.
Aufgabenstellung
Einladungskarte "Sommerempfang" - Coverseite
Wir benötigen eine Coverseite DIN Lang (210mm x 100 mm) für die Einladungskarte unseres diesjährigen Sommerempfangs.
Der Sommerempfang wird wie jedes Jahr von zwei Institutionen ausgerichtet - von der Heilkundlichen Gemeinschaft (HG) Südwestfalen und der Medizinerbund Ostmark (mbom).
Aus diesem Grund müssen auch die beiden CI Farben in dem Schriftzug "Sommerempfang" enthalten sein - rot vorderer Teil - grün hinterer Teil.
Zusammengefasst:
Die Farben müssen Verwendung finden:
Rot HG Südwestfalen (c 30 | m 100 | y 90 | k 0)
Grün Medizinerbund Ostmark (c 75 | m 5 | y 100 | k 0)
Die Coverseite kann „moderner“ und abstrakter (Beispiel 2016) als die der vergangenen Anfangsjahren des Sommerempfangs gestaltet werden.
Der Schriftzug „Sommerempfang“ muss auf der Coverseite enthalten sein.
Kann/soll aber neu von der Schriftart her gestaltet werden.
Der Schriftzug Sommerempfang – ist unterteilt in rot und grün
(gemeinsame Veranstaltung | Hausfarben der Ausrichter - s.o.)
Der Schriftzug „am 27. September 2017 im Halle am Lindenhof“ kann frei platziert und gestaltet werden.

```html
<!DOCTYPE html>
<html lang="de">
<head>
<meta charset="utf-8">
<title>Sommerempfang – Einladungskarte Cover</title>
<link rel="stylesheet" href="https://fonts.googleapis.com/css2?family=Roboto:wght@300;900&display=swap">
<style>
  :root {
    --page-bg: #e4e4e4;
    --green: #3fa535;
    --red: #b31b2c;
    --band: #ffffff;
    --leaf-dark: #2f7d2a;
    --leaf-mid: #5cae45;
    --leaf-light: #c4e0a6;
  }
  html, body {
    margin: 0;
    width: 1200px;
    height: 800px;
    overflow: hidden;
    background: var(--page-bg);
  }
  .invitation-cover {
    position: absolute;
    left: 40px;
    top: 133px;
    width: 1120px;
    height: 533px;
    overflow: hidden;
  }
  .foliage-photo {
    position: absolute;
    inset: 0;
    background:
      radial-gradient(ellipse 60% 30% at 50% 0%, var(--leaf-dark) 0%, transparent 100%),
      linear-gradient(180deg, var(--leaf-dark) 0%, var(--leaf-mid) 25%, var(--leaf-light) 48%, #9fcf7f 70%, #7dbf5e 100%);
  }
  .title-band {
    position: absolute;
    left: 0;
    top: 387px;
    width: 100%;
    height: 83px;
    background: var(--band);
    display: flex;
    align-items: center;
    font-family: "Roboto", Arial, sans-serif;
  }
  .event-title {
    margin: 0 0 0 42px;
    font-weight: 900;
    font-size: 80px;
    line-height: 1;
    letter-spacing: -1px;
    white-space: nowrap;
  }
  .event-title .part-front { color: var(--red); }
  .event-title .part-back { color: var(--green); }
  .event-details {
    position: absolute;
    left: 778px;
    top: 12px;
    margin: 0;
    font-weight: 300;
    font-size: 26px;
    line-height: 33px;
    color: var(--green);
    letter-spacing: 0.3px;
    white-space: nowrap;
  }
</style>
</head>
<body>
  <section class="invitation-cover">
    <div class="foliage-photo" role="img" aria-label="Foto: hängende grüne Blätterzweige vor unscharfem, sonnigem Grün mit Lichtreflexen"></div>
    <div class="title-band">
      <h1 class="event-title"><span class="part-front">SOMMER</span><span class="part-back">EMPFANG</span></h1>
      <p class="event-details">am 27. September 2017<br>im Halle am Lindenhof</p>
    </div>
  </section>
</body>
</html>
```